Postcard Design

We are a commercial real estate office located in Mount Kisco. We are holding a rather large event on August 6th for our tenants and in each give a way bag we would like to put a post card. This post card will feature 4 of our buildings on it. We would also like it to say something along the lines of Looking for Office, Medical, Warehouse or Retail space or know someone who is?? Fill out this post card with either your information or the information of a referral & send it back to receive a $25 Gift Card to Velvet Lanes, NY. The point of the post card is to get all guests to refer a friend who is looking for a space. We do need space for an address but we also do need a space on the back that has room for them to fill out all necessary information such as - Name - Email- Referral Name- Phone Number -
Also on the card we would like it to say for all space availabilities visit www.harborlinerealty.example along with some of our contact information. The building information is as follows - the picture with the flowers is 48 Quillfern Ave, N. White Plains, the building with the grass round about in front of it is 212 W Tamsworth Ln. Mount Kisco, the picture that has the close up of the building that is more of a square building is 417/419 W Tamsworth Ln, Mount Kisco and the building with the clouds that is set far back is 586 East Tamsworth Ln, Mount Kisco

NOTE I need all four buildings on the post card. Not just 1. Please list the building addresses by each picture

The name of our company is Harborline Realty - our phone number is 914 608 3157 and the contact for all inquiries is Owen Trezelle

Target Market(s)

Brokers and business owners

Industry/Entity Type

Real Estate

Colors
0455a3
85abd2
3276b5

Requirements
Must have
• We are a commercial real estate office so we would like this post card to be catchy.

```html
<!DOCTYPE html>
<html lang="en">
<head>
<meta charset="utf-8">
<title>Harborline Realty Referral Postcard</title>
<link rel="stylesheet" href="https://fonts.googleapis.com/css2?family=Oswald:wght@700&family=Roboto+Condensed:wght@400;700&family=Libre+Baskerville&display=swap">
<style>
  :root {
    --page-bg: #5c5d5f;
    --card-bg: #ffffff;
    --red: #d42129;
    --blue: #5571b5;
    --ink: #1f1f1f;
    --tile: #dfe3f3;
    --bar: #1c1c1c;
    --bar-blue: #8fa6d6;
  }
  * { box-sizing: border-box; margin: 0; padding: 0; }
  html, body { width: 958px; height: 1200px; overflow: hidden; }
  body { background: var(--page-bg); position: relative; font-family: "Roboto Condensed", "Arial Narrow", sans-serif; }
  .postcard { position: absolute; left: 77px; top: 78px; width: 803px; height: 1045px; background: var(--card-bg); }
  .headline {
    position: absolute; left: 0; top: 5px; width: 100%; text-align: center; white-space: nowrap;
    font-family: "Oswald", "Arial Narrow", sans-serif; font-weight: 700;
    font-size: 122px; line-height: 1; color: var(--red); letter-spacing: 3px;
  }
  .subhead {
    position: absolute; left: 0; top: 153px; width: 100%; text-align: center; white-space: nowrap;
    font-weight: 700; font-size: 42px; line-height: 50px; color: var(--blue); text-transform: uppercase;
  }
  .offer {
    position: absolute; left: 30px; top: 262px; width: 560px; text-align: center; white-space: nowrap;
    font-size: 34px; line-height: 36px; color: var(--ink);
  }
  .gift-badge {
    position: absolute; left: 575px; top: 245px; width: 196px; height: 196px;
    border-radius: 50%; background: var(--red); color: #fff; z-index: 2;
  }
  .gift-badge .badge-text {
    position: absolute; left: 0; top: 24px; width: 100%; text-align: center;
    transform: rotate(14deg); font-weight: 700;
  }
  .badge-amount { display: block; font-size: 48px; line-height: 48px; }
  .badge-label { display: block; font-size: 25px; line-height: 25px; }
  .property { position: absolute; width: 367px; height: 218px; background: var(--tile); }
  .property-photo { position: absolute; left: 12px; top: 12px; width: 343px; height: 130px; border: 2px solid #fff; }
  .property-street { position: absolute; left: 14px; top: 155px; font-weight: 700; font-size: 22px; color: var(--ink); text-transform: uppercase; white-space: nowrap; }
  .property-city { position: absolute; left: 14px; top: 182px; font-size: 21px; color: var(--ink); white-space: nowrap; }
  .p1 { left: 21px; top: 392px; }
  .p2 { left: 416px; top: 392px; }
  .p3 { left: 21px; top: 627px; }
  .p4 { left: 416px; top: 627px; }
  .photo-garden { background: linear-gradient(180deg, #6f93c9 0%, #4a7a3a 55%, #2f7a2a 100%); }
  .photo-office { background: linear-gradient(180deg, #4fa2e0 0%, #d8c79a 55%, #7b8a78 100%); }
  .photo-block { background: linear-gradient(180deg, #3b8fd6 0%, #e6e0d4 45%, #6e6a5c 100%); }
  .photo-warehouse { background: linear-gradient(180deg, #3c86d2 0%, #dde6ef 35%, #4d7a3d 60%, #8a8c8e 100%); }
  .availability-bar {
    position: absolute; left: 21px; top: 869px; width: 762px; height: 41px; background: var(--bar);
    text-align: center; font-weight: 700; font-size: 23px; line-height: 41px; color: #fff; text-transform: uppercase; white-space: nowrap;
  }
  .availability-bar .lead { color: var(--bar-blue); }
  .brand { position: absolute; left: 21px; top: 928px; display: flex; align-items: center; }
  .brand-square { width: 80px; height: 92px; background: var(--blue); }
  .brand-name {
    margin-left: 12px; font-family: "Libre Baskerville", Georgia, serif; font-size: 31px; line-height: 36px; color: var(--ink);
  }
  .divider { position: absolute; left: 301px; top: 932px; width: 1px; height: 90px; background: #9a9a9a; }
  .contact { position: absolute; left: 310px; top: 946px; width: 480px; text-align: center; white-space: nowrap; }
  .contact-label { font-size: 24px; color: var(--ink); text-transform: uppercase; }
  .contact-line { margin-top: 8px; font-weight: 700; font-size: 32px; color: var(--blue); text-transform: uppercase; }
</style>
</head>
<body>
  <main class="postcard">
    <h1 class="headline">LOOKING FOR</h1>
    <p class="subhead">Office, Medical, Warehouse or Retail<br>Space or know someone who is??</p>
    <p class="offer">Fill out this post card with either your<br>information or the information of a<br>referral &amp; send it back to receive a</p>
    <div class="gift-badge">
      <div class="badge-text">
        <span class="badge-amount">$25</span>
        <span class="badge-label">Gift Card to</span>
        <span class="badge-label">VELVET</span>
        <span class="badge-label">LANES, NY.</span>
      </div>
    </div>

    <section class="property p1">
      <div class="property-photo photo-garden" role="img" aria-label="Curved office building behind flowering shrubs and lawn"></div>
      <p class="property-street">48 Quillfern Avenue</p>
      <p class="property-city">North White Plains, NY 10603</p>
    </section>
    <section class="property p2">
      <div class="property-photo photo-office" role="img" aria-label="Long three-storey office building with a grass roundabout in front"></div>
      <p class="property-street">212 West Tamsworth Lane</p>
      <p class="property-city">Mt. Kisco, NY 10549</p>
    </section>
    <section class="property p3">
      <div class="property-photo photo-block" role="img" aria-label="Close view of a square white three-storey office building"></div>
      <p class="property-street">417-419 West Tamsworth Lane</p>
      <p class="property-city">Mt. Kisco, NY 10549</p>
    </section>
    <section class="property p4">
      <div class="property-photo photo-warehouse" role="img" aria-label="Low brick warehouse set back behind a parking lot under a cloudy sky"></div>
      <p class="property-street">586 East Tamsworth Lane</p>
      <p class="property-city">Mount Kisco, NY 10549.</p>
    </section>

    <div class="availability-bar"><span class="lead">All space availabilities visit</span> www.harborlinerealty.example</div>

    <div class="brand">
      <div class="brand-square"></div>
      <p class="brand-name">Harborline<br>Realty</p>
    </div>
    <div class="divider"></div>
    <div class="contact">
      <p class="contact-label">Contact for all inquiries</p>
      <p class="contact-line">Owen Trezelle : 914 608 3157</p>
    </div>
  </main>
</body>
</html>
```